General contractor/GM consaltant business card

I need a card for my contracting company in North Dakota, we build industrial buildings for the oil feild and oil feild related companies offices, shops, airplain hangars, airports ext. We have a familly atmosphere on the job and are very relational and personal.
Industry/Entity Type
Industrial
Contact Information for Business Card
Kestrelmoor Builders LLC.
Dwight T.Halvorsun
4736 Quillfern dr. Colorado Springs, CO. 80927
Cell# 406-555-8142
dwight@kestrelmoorbuilders.com

```html
<!DOCTYPE html>
<html lang="en">
<head>
<meta charset="utf-8">
<title>Kestrelmoor Builders LLC – Business Card</title>
<link rel="stylesheet" href="https://fonts.googleapis.com/css2?family=Marcellus&family=Open+Sans:wght@400;600&display=swap">
<style>
  :root {
    --backdrop: #a9a9a9;
    --brand-blue: #1d5893;
    --brand-blue-deep: #174a7e;
    --card-white: #ffffff;
    --accent-red: #e2452b;
    --ink: #1c1c1c;
    --haze-light: rgba(255,255,255,0.10);
    --haze-grey: rgba(150,160,170,0.18);
  }
  * { box-sizing: border-box; margin: 0; padding: 0; }
  html, body { width: 1200px; height: 900px; overflow: hidden; }
  body {
    background: var(--backdrop);
    font-family: "Open Sans", Arial, sans-serif;
    position: relative;
  }
  .card {
    position: absolute;
    top: 300px;
    width: 520px;
    height: 300px;
    border-radius: 22px;
    overflow: hidden;
    box-shadow: 0 14px 26px rgba(0,0,0,0.28);
  }
  .card--front { left: 50px; background: var(--brand-blue); }
  .card--back  { left: 630px; background: var(--card-white); }

  .scenery {
    position: absolute;
    right: 0; top: 0; bottom: 0;
    width: 62%;
  }
  .card--front .scenery {
    background: linear-gradient(90deg, rgba(255,255,255,0) 0%, var(--haze-light) 45%, rgba(255,255,255,0.06) 100%);
  }
  .card--back .scenery {
    background: linear-gradient(90deg, rgba(255,255,255,0) 0%, var(--haze-grey) 50%, rgba(150,160,170,0.10) 100%);
  }

  .brand {
    position: absolute;
    display: flex;
    align-items: center;
    gap: 14px;
    font-family: "Marcellus", Georgia, serif;
  }
  .brand__dot {
    width: 56px; height: 56px;
    border-radius: 50%;
    flex: none;
  }
  .brand__name { line-height: 1; }
  .brand__primary { display: block; font-size: 42px; letter-spacing: 0.5px; }
  .brand__secondary { display: block; font-size: 22px; letter-spacing: 5px; margin-top: 4px; }

  .card--front .brand { left: 56px; top: 108px; color: var(--card-white); }
  .card--front .brand__dot { background: var(--card-white); }
  .card--back .brand { left: 46px; top: 40px; color: var(--brand-blue); }
  .card--back .brand__dot { background: var(--brand-blue); }

  .front-address {
    position: absolute;
    left: 30px; right: 20px; top: 232px;
    font-family: "Marcellus", Georgia, serif;
    font-size: 19px;
    color: var(--card-white);
    letter-spacing: 0.3px;
  }

  .name-band {
    position: absolute;
    left: 0; right: 0; top: 140px;
    height: 52px;
    background: var(--brand-blue);
    color: var(--card-white);
    text-align: center;
    padding-top: 4px;
  }
  .name-band__name { font-size: 20px; font-weight: 400; line-height: 1.2; }
  .name-band__role { font-size: 13px; line-height: 1.2; }

  .contact-list {
    position: absolute;
    right: 22px; top: 208px;
    list-style: none;
    text-align: right;
    color: var(--ink);
    font-size: 13px;
    line-height: 22px;
  }
  .contact-list__item { display: flex; justify-content: flex-end; align-items: center; gap: 8px; }
  .contact-list__icon { width: 13px; height: 11px; flex: none; }
  .contact-list__spacer { width: 13px; flex: none; }
</style>
</head>
<body>

  <section class="card card--front" aria-label="Business card front">
    <div class="scenery" role="img" aria-label="Faint silhouettes of oil field derricks"></div>
    <div class="brand">
      <span class="brand__dot"></span>
      <span class="brand__name">
        <span class="brand__primary">Kestrelmoor</span>
        <span class="brand__secondary">Builders LLC</span>
      </span>
    </div>
    <p class="front-address">4736 Quillfern dr. Colorado Springs, CO. 80927</p>
  </section>

  <section class="card card--back" aria-label="Business card back">
    <div class="scenery" role="img" aria-label="Faint silhouettes of oil field derricks"></div>
    <div class="brand">
      <span class="brand__dot"></span>
      <span class="brand__name">
        <span class="brand__primary">Kestrelmoor</span>
        <span class="brand__secondary">Builders LLC</span>
      </span>
    </div>
    <div class="name-band">
      <p class="name-band__name">Dwight T.Halvorsun</p>
      <p class="name-band__role">Designation</p>
    </div>
    <ul class="contact-list">
      <li class="contact-list__item">406-555-8142
        <svg class="contact-list__icon" viewBox="0 0 13 11" aria-hidden="true">
          <path d="M1 4 Q6.5 0 12 4 L10.5 5.5 L9 4.5 L4 4.5 L2.5 5.5 Z" fill="var(--accent-red)"/>
          <rect x="3" y="5.5" width="7" height="5" rx="1" fill="var(--accent-red)"/>
        </svg>
      </li>
      <li class="contact-list__item">dwight@kestrelmoorbuilders.com
        <svg class="contact-list__icon" viewBox="0 0 13 11" aria-hidden="true">
          <rect x="0.5" y="1.5" width="12" height="8" fill="var(--accent-red)"/>
          <path d="M0.5 1.5 L6.5 6 L12.5 1.5" stroke="#fff" stroke-width="1" fill="none"/>
        </svg>
      </li>
      <li class="contact-list__item">4736 Quillfern dr. Colorado Springs, CO. 80927<span class="contact-list__spacer"></span></li>
    </ul>
  </section>

</body>
</html>
```